nine-parts.com

We are a small dollar lending company that will revolutionize the industry. We will do this by being completely transparent, fee free, etc and an interest rate that normal people can afford to pay. Over 10X less than our competition. We only allow our members to pay bills " bills paid fast", within 72 hours. Payday loans typically charge from 390%-600% with a terrible payback structure. We charge 9parts, period, with a payback structure over 12 months. Our site will be very simple and easy to use but elegant at the same time. We do not want the site to be too busy, less is more and easier. We will have; Home, The Story, Why 9parts.com, Are you eligible? Members, Clients. To become a member you have to be referred by a current client of 9parts.com. A lot of the busy stuff will be saved for the Members and Clients sections. The feel must be elegant, easy to use and very simple to understand. I am looking for the green, white and black combinations of colors, very similar to my logo that was designed by Pixelmoor.

```html
<!DOCTYPE html>
<html lang="en">
<head>
<meta charset="utf-8">
<title>nine-parts.com</title>
<link href="https://fonts.googleapis.com/css2?family=Ubuntu:ital,wght@0,400;0,500;1,400;1,500&display=swap" rel="stylesheet">
<style>
:root{
  --green:#8cc63f;
  --green-dark:#6fab24;
  --ink:#2a2a2a;
  --text:#5a5a5a;
  --footer-text:#c8c8c8;
  --white:#ffffff;
}
*{margin:0;padding:0;box-sizing:border-box}
html,body{width:1164px;height:1200px;overflow:hidden;background:var(--white);font-family:"Ubuntu",sans-serif;color:var(--text)}
.page{position:relative;width:1164px;height:1200px}
.topline{position:absolute;top:0;left:0;width:100%;height:6px;background:#f1f1f1}
.brand{position:absolute;left:118px;top:14px;display:flex;align-items:center;gap:12px}
.brand-dot{width:56px;height:56px;border-radius:50%;background:var(--green)}
.brand-name{font-size:34px;font-weight:400;color:var(--ink);letter-spacing:-.5px}
.member-tab{position:absolute;left:854px;top:6px;width:184px;height:31px;background:#ececec;clip-path:polygon(0 0,100% 0,96% 100%,4% 100%);display:flex;align-items:center;justify-content:center;gap:9px;color:var(--green-dark);font-size:14px}
.nav{position:absolute;left:411px;top:69px;display:flex;list-style:none}
.nav li{height:33px;line-height:33px;padding:0 11px;font-size:12.5px;color:var(--ink);letter-spacing:.3px;white-space:nowrap}
.nav li.active{background:var(--green);color:var(--white);padding:0 18px;margin-right:1px}
.hero-band{position:absolute;left:0;top:113px;width:100%;height:442px;background:linear-gradient(#2c2c2c,#3a3a3a)}
.slider{position:absolute;left:126px;top:138px;width:912px;height:394px;border:4px solid #d8d8d8;background:linear-gradient(90deg,#6d6d6d 0%,#9a9a9a 35%,#b8b8b8 60%,#8c97a8 100%);overflow:hidden}
.slider-photo{position:absolute;right:0;top:0;width:560px;height:100%;background:linear-gradient(90deg,rgba(180,180,180,0) 0%,#a9b6c9 40%,#7f90ab 100%)}
.slider-copy{position:absolute;left:32px;top:90px;font-size:33px;font-weight:500;line-height:37px;color:var(--white);text-shadow:0 1px 2px rgba(0,0,0,.35)}
.slider-copy em{font-style:normal;color:var(--green)}
.slider-btn{position:absolute;left:32px;top:230px;width:194px;height:43px;background:linear-gradient(#94cd45,#7cb832);color:var(--white);font-size:21px;display:flex;align-items:center;justify-content:center;letter-spacing:.3px}
.slider-dots{position:absolute;left:396px;bottom:0;width:148px;height:31px;background:#1e1e1e;clip-path:polygon(8% 0,92% 0,100% 100%,0 100%);display:flex;align-items:center;justify-content:center;gap:8px}
.slider-dots span{width:14px;height:14px;border-radius:50%;background:var(--white)}
.slider-dots span.on{background:var(--green)}
.about{position:absolute;left:126px;top:584px;width:602px}
h2{font-size:24px;font-weight:400;color:var(--ink)}
.about p{margin-top:14px;font-size:13px;line-height:22.4px}
.btn{display:inline-flex;align-items:center;justify-content:center;width:120px;height:36px;color:var(--white);font-size:15px}
.btn-green{background:linear-gradient(#94cd45,#7cb832)}
.btn-dark{background:linear-gradient(#3c3c3c,#222)}
.about .btn{margin-top:26px}
.divider{margin-top:23px;border:0;border-top:1px solid #dcdcdc}
.client h2{margin-top:12px}
.quote{margin-top:12px;font-style:italic;font-size:13px;line-height:19.5px;position:relative;text-indent:42px}
.quote .mark{position:absolute;left:6px;top:-6px;font-size:44px;line-height:40px;color:var(--green);font-weight:500;text-indent:0;font-style:normal}
.quote .end{color:var(--green);font-size:42px;line-height:10px;font-weight:500;font-style:normal;vertical-align:-16px;margin-left:6px}
.author{margin-top:10px;font-style:italic;font-size:13px;line-height:18px}
.author strong{color:var(--green-dark);font-weight:500}
.why{position:absolute;left:747px;top:589px;width:291px;height:390px;background:var(--green);padding:20px 21px}
.why h2{color:var(--ink)}
.why-photo{margin-top:14px;width:249px;height:137px;background:linear-gradient(#6aa3e0,#a9cff2)}
.why p{margin-top:12px;font-size:13.5px;line-height:22.4px;color:var(--white)}
.why .btn{margin-top:19px}
.footer{position:absolute;left:0;top:1012px;width:100%;height:188px;background:linear-gradient(#3a3a3a,#444)}
.foot-nav{position:absolute;left:126px;top:40px;display:flex;gap:29px;list-style:none;font-size:11.5px;letter-spacing:.6px;color:var(--footer-text)}
.connect{position:absolute;left:905px;top:40px;font-size:12.5px;color:var(--white);letter-spacing:.5px}
.social{position:absolute;left:907px;top:66px;display:flex;gap:6px}
.social span{width:29px;height:29px;border-radius:4px}
.foot-brand{position:absolute;left:126px;top:94px;display:flex;align-items:center;gap:8px}
.foot-brand .brand-dot{width:26px;height:26px}
.foot-brand span{font-size:15px;color:var(--white)}
.legal{position:absolute;left:204px;top:132px;font-size:11.5px;line-height:19px;color:#b0b0b0;letter-spacing:.5px}
</style>
</head>
<body>
<div class="page">
  <div class="topline"></div>
  <div class="brand"><div class="brand-dot"></div><span class="brand-name">nine-parts</span></div>
  <div class="member-tab">
    <svg width="16" height="16" viewBox="0 0 16 16" aria-hidden="true"><circle cx="8" cy="4.5" r="3.5" fill="#555"/><path d="M1 16c0-4 3-6.5 7-6.5s7 2.5 7 6.5z" fill="#555"/></svg>
    Member Area
  </div>
  <ul class="nav">
    <li class="active">HOME</li><li>THE STORY</li><li>WHY 9PARTS.COM</li><li>ARE YOU ELIGIBLE? MEMBERS</li><li>CLIENTS</li><li>CONTACT</li>
  </ul>

  <div class="hero-band"></div>
  <div class="slider">
    <div class="slider-photo" role="img" aria-label="Man in a striped shirt holding out a fan of dollar bills"></div>
    <div class="slider-copy">With the money <em>we lend</em> we<br>will allow people only to<br><em>pay bills.</em></div>
    <div class="slider-btn">Bills Paid Fast</div>
    <div class="slider-dots"><span class="on"></span><span></span><span></span><span></span></div>
  </div>

  <section class="about">
    <h2>About 9parts</h2>
    <p>Aliquam molestie, mi et imperdiet euismod, dui purus auctor tellus, et interdum lacus lectus et ante. Sed accumsan sollicitudin sapien, sit amet adipiscing turpis gravida ac. In congue, neque ac lobortis volutpat, libero mauris varius mi, vitae suscipit ipsum ligula vitae risus. Duis aliquam nibh a dui iaculis viverra id a velit. Vivamus egestas risus in magna varius commodo. Sed semper viverra egestas. Etiam pretium porttitor lectus, vel ornare neque porta volutpat.</p>
    <a class="btn btn-green">Read More</a>
    <hr class="divider">
    <div class="client">
      <h2>Client Says...</h2>
      <p class="quote"><span class="mark">&ldquo;</span>Aliquam molestie, mi et imperdiet euismod, dui purus auctor tellus, et interdum lacus lectus et ante. Sed accumsan sollicitudin sapien, sit amet adipiscing turpis gravida ac. In congue, neque ac lobortis volutpat, libero mauris varius mi, vitae suscipit ipsum ligula vitae risus....<span class="end">&rdquo;</span></p>
      <p class="author"><strong>-Dana Whitfield</strong><br>Location name here</p>
    </div>
  </section>

  <aside class="why">
    <h2>Why 9parts.com</h2>
    <div class="why-photo" role="img" aria-label="Raised hands holding dollar bills against a blue sky"></div>
    <p>Aenean a nibh eget turpis vehicula tempus ac sed massa. Vestibulum dolor nulla, ultrices ac tincidunt sed, laoreet non est. Suspendisse lobortis turpis in odio blandit ac interdum lorem...</p>
    <a class="btn btn-dark">Read More</a>
  </aside>

  <footer class="footer">
    <ul class="foot-nav"><li>HOME</li><li>THE STORY</li><li>WHY 9PARTS.COM</li><li>ARE YOU ELIGIBLE? MEMBERS</li><li>CLIENTS</li><li>CONTACT</li></ul>
    <div class="connect">CONNECT US:</div>
    <div class="social">
      <span style="background:#4a6ea9"></span><span style="background:#5cc6e8"></span><span style="background:#2f7bbd"></span><span style="background:#f08a24"></span>
    </div>
    <div class="foot-brand"><div class="brand-dot"></div><span>nine-parts</span></div>
    <div class="legal">Copyright &copy; 2014. All Right Reserved<br>Term of Services</div>
  </footer>
</div>
</body>
</html>
```